Menu Revamp

FIRST TASK
------------------
I just want somebody to make my website menu look better
Assets which can be used are here https://www.filebarrow.example/sh/qpxlmvdrkaz7ne/BBHrTN8pqweKLmZYwRcVbxK4tu?dl=0
However the designer can take from assets which are already on the www.lucasferny.com website

this is the previous design that was done but it does not look so good

The designer will have to be logical in building the menu and carefully place assets as we want this menu to make. the user want to browse our collections , know our history - "it has to sell and look good''

Please do a mobile. tablet and desktop. version. please - I will ask for the PSD files in. the end

SECOND TASK
-------------------------
We have an auction platform and we want to design a dasboard. where the user can. manage their bids. This is the sketch https://linkstub.example/k7pqmrzd

Can you please make it look like with a nice feel to it, classy

Number of Pages Required

1 page

```html
<!DOCTYPE html>
<html lang="en">
<head>
<meta charset="utf-8">
<title>Lucas Ferny – Menu</title>
<link href="https://fonts.googleapis.com/css2?family=Jost:wght@300;400&display=swap" rel="stylesheet">
<style>
  :root{
    --bar-top:#e9e9e9;
    --bar-nav:#f4f4f4;
    --page:#ffffff;
    --ink:#1c1c1c;
    --muted:#8a8a8a;
    --field:#f6f6f6;
  }
  *{box-sizing:border-box;margin:0;padding:0}
  html,body{width:1200px;height:329px;overflow:hidden;background:var(--page)}
  body{position:relative;font-family:'Jost',sans-serif;color:var(--ink)}
  .header{position:absolute;left:0;width:1200px;height:112.5px}
  .header--default{top:0}
  .header--active{top:137.5px}
  .header__top{position:absolute;left:0;top:0;width:100%;height:62.5px;background:var(--bar-top)}
  .header__nav{position:absolute;left:0;top:62.5px;width:100%;height:50px;background:var(--bar-nav)}
  .nav-list{position:absolute;left:237.5px;top:0;height:50px;display:flex;gap:24px}
  .brand{position:absolute;left:600px;top:31px;transform:translate(-50%,-50%);font-weight:400;font-size:14px;letter-spacing:.08em;white-space:nowrap;color:var(--ink)}
  .icon{position:absolute;top:18px}
  .icon--search{left:836px}
  .icon--cart{left:883px}
  .icon--user{left:940px}
  .cart-count{position:absolute;left:898px;top:33px;width:19px;height:19px;border-radius:50%;background:var(--ink);color:#fff;font-size:8px;display:flex;align-items:center;justify-content:center}
  .nav-link{height:50px;line-height:50px;font-size:11.5px;font-weight:300;letter-spacing:.04em;text-transform:uppercase;white-space:nowrap}
  .lang{position:absolute;left:924px;top:17px;display:flex;align-items:center;gap:4px;font-size:12px;font-weight:300}
  .lang__code{border-bottom:1px solid #bdbdbd;line-height:13px}
  .search-field{position:absolute;left:666px;top:14px;width:200px;height:35px;border-radius:7px;background:var(--field)}
  .search-field__text{position:absolute;left:14px;top:8px;font-size:14px;font-weight:300;color:var(--muted);letter-spacing:.03em;border-left:1px solid var(--muted);padding-left:4px;line-height:18px}
  .search-field .icon--search{left:170px;top:4px}
  .account-tab{position:absolute;left:929px;top:0;width:46px;height:62.5px;background:var(--page);border-radius:8px 8px 0 0}
  .account-panel{position:absolute;left:787.5px;top:200px;width:187.5px;height:129px;background:var(--page);border-radius:8px 0 0 0;z-index:2}
  .field{position:absolute;left:12.5px;width:162.5px;height:25px;border:1.3px solid var(--ink);border-radius:13px;font-size:11px;font-weight:300;padding-left:10px;line-height:22px}
  .field--email{top:17.5px}
  .field--password{top:53.75px;color:var(--muted)}
  .field__label{position:absolute;left:11px;top:-5px;background:var(--page);padding:0 2px;font-size:6px;line-height:8px;letter-spacing:.05em;color:var(--ink)}
  .field__caret{display:inline-block;width:1px;height:12px;background:var(--ink);vertical-align:middle}
  .field--password .field__caret{background:var(--muted);margin-right:3px}
  .btn{position:absolute;top:91px;height:25px;border-radius:13px;font-size:11.5px;font-weight:300;letter-spacing:.05em;display:flex;align-items:center;justify-content:center}
  .btn--primary{left:12.5px;width:69px;background:var(--ink);color:#fff}
  .btn--outline{left:103px;width:72px;border:1.3px solid var(--ink)}
  .or{position:absolute;left:91px;top:100px;font-size:6px;letter-spacing:.05em}
</style>
</head>
<body>

<header class="header header--default">
  <div class="header__top">
    <span class="brand">LUCAS FERNY</span>
    <svg class="icon icon--search" width="26" height="26" viewBox="0 0 26 26" fill="none" stroke="#1c1c1c" stroke-width="1.4"><circle cx="11" cy="11" r="9.5"/><line x1="18" y1="18" x2="25" y2="25"/></svg>
    <svg class="icon icon--cart" width="26" height="26" viewBox="0 0 26 26" fill="none" stroke="#1c1c1c" stroke-width="1.4"><path d="M1.5 4.5h23v20h-23z"/><path d="M8 4.5a5 5 0 0 1 10 0"/><path d="M8 9a5 5 0 0 0 10 0"/></svg>
    <span class="cart-count">0</span>
    <svg class="icon icon--user" width="24" height="26" viewBox="0 0 24 26" fill="none" stroke="#1c1c1c" stroke-width="1.4"><circle cx="12" cy="8" r="6.5"/><path d="M1 25v-3a6 6 0 0 1 6-6h10a6 6 0 0 1 6 6v3z"/></svg>
  </div>
  <nav class="header__nav">
    <div class="nav-list">
      <span class="nav-link">Jewellery</span>
      <span class="nav-link">Pearl Bar</span>
      <span class="nav-link">Ferny Select Collections</span>
      <span class="nav-link">Our Story</span>
      <span class="nav-link">Stores</span>
      <span class="nav-link">Blog</span>
      <span class="nav-link">Contact Us</span>
    </div>
    <span class="lang">
      <svg width="9" height="9" viewBox="0 0 10 10"><circle cx="5" cy="5" r="5" fill="#2b3f8c"/><path d="M0 5h10M5 0v10" stroke="#fff" stroke-width="2.4"/><path d="M0 5h10M5 0v10" stroke="#c8202f" stroke-width="1.2"/></svg>
      <span class="lang__code">EN</span>
      <svg width="6" height="4" viewBox="0 0 6 4" fill="none" stroke="#1c1c1c" stroke-width="0.8"><path d="M.5.5 3 3 5.5.5"/></svg>
    </span>
  </nav>
</header>

<header class="header header--active">
  <div class="header__top">
    <span class="brand">LUCAS FERNY</span>
    <div class="search-field">
      <span class="search-field__text">Search...</span>
      <svg class="icon icon--search" width="26" height="26" viewBox="0 0 26 26" fill="none" stroke="#1c1c1c" stroke-width="1.4"><circle cx="11" cy="11" r="9.5"/><line x1="18" y1="18" x2="25" y2="25"/></svg>
    </div>
    <svg class="icon icon--cart" width="26" height="26" viewBox="0 0 26 26" fill="none" stroke="#1c1c1c" stroke-width="1.4"><path d="M1.5 4.5h23v20h-23z"/><path d="M8 4.5a5 5 0 0 1 10 0"/><path d="M8 9a5 5 0 0 0 10 0"/></svg>
    <span class="cart-count">1</span>
    <div class="account-tab"></div>
    <svg class="icon icon--user" width="24" height="26" viewBox="0 0 24 26" fill="none" stroke="#1c1c1c" stroke-width="1.4"><circle cx="12" cy="8" r="6.5"/><path d="M1 25v-3a6 6 0 0 1 6-6h10a6 6 0 0 1 6 6v3z"/></svg>
  </div>
  <nav class="header__nav">
    <div class="nav-list">
      <span class="nav-link">Jewellery</span>
      <span class="nav-link">Pearl Bar</span>
      <span class="nav-link">Ferny Select Collections</span>
      <span class="nav-link">Our Story</span>
      <span class="nav-link">Stores</span>
      <span class="nav-link">Blog</span>
      <span class="nav-link">Contact Us</span>
    </div>
  </nav>
</header>

<form class="account-panel">
  <div class="field field--email"><span class="field__label">EMAIL</span>Marcus Pellow<span class="field__caret"></span></div>
  <div class="field field--password"><span class="field__caret"></span>Password...</div>
  <span class="btn btn--primary">SIGN IN</span>
  <span class="or">OR</span>
  <span class="btn btn--outline">SIGN UP</span>
</form>

</body>
</html>
```